Email Signature

We are looking for creative email signature for our company. Please find attached the logo of our company for your reference. now we understand there isn't much can be done with email signature but we are looking for out of the box designs. Nothing specific in mind

Please insert fake numbers, website and/or address, etc just to showcase the designs. once the design is chosen we will provide the actual details.
Updates

Dear All,

We wouldlike to extend our apology for not being able to provide feedbacks to everysingle design. We were extremely busy and we have multiple contests opensimultaneously which makes the process harder. However, thank you all for theefforts you have put into this contest. We have received anoverwhelming quality responses & it has been a very difficult task tochoose just one, we easily Loved at least several designs...

Thanksagain for participating, we wish you all success in your design ventures.

Kindregards,

HLW Team

Industry/Entity Type

It Company

```html
<!DOCTYPE html>
<html lang="en">
<head>
<meta charset="utf-8">
<title>Harbor Lantern Works – Email Signature</title>
<link rel="stylesheet" href="https://fonts.googleapis.com/css2?family=Arimo:wght@700&display=swap">
<style>
  :root {
    --brand-blue: #0f82dc;
    --frame-grey: #403c3c;
    --paper: #ffffff;
  }
  html, body {
    margin: 0;
    padding: 0;
    overflow: hidden;
    background: var(--paper);
  }
  .signature {
    position: relative;
    width: 1200px;
    height: 1000px;
    background: var(--paper);
    font-family: "Arimo", Arial, sans-serif;
    font-weight: 700;
    color: var(--brand-blue);
  }
  .arrow-frame {
    position: absolute;
    left: 0;
    top: 0;
  }
  .brand-name {
    position: absolute;
    left: 322px;
    top: 205px;
    margin: 0;
    font-size: 94px;
    line-height: 166px;
    letter-spacing: -3px;
    font-weight: 700;
    color: var(--brand-blue);
  }
  .brand-name span {
    display: block;
  }
  .address {
    position: absolute;
    left: 324px;
    top: 574px;
    margin: 0;
    font-style: normal;
    font-size: 36px;
    line-height: 50px;
    letter-spacing: 0.5px;
  }
  .address span {
    display: block;
  }
  .website {
    position: absolute;
    left: 323px;
    top: 760px;
    margin: 0;
    font-size: 36px;
    letter-spacing: 0.5px;
  }
</style>
</head>
<body>
  <div class="signature">
    <svg class="arrow-frame" width="1200" height="1000" viewBox="0 0 1200 1000" aria-hidden="true">
      <path d="M304 182 H612 V56 Q612 44 622 50 L966 474 Q972 480 966 488 L622 940 Q612 948 612 936 V812 H304 Q296 812 296 804 V190 Q296 182 304 182 Z"
            fill="var(--paper)" stroke="var(--frame-grey)" stroke-width="16" stroke-linejoin="round"/>
    </svg>

    <h1 class="brand-name">
      <span>Harbor</span>
      <span>Lantern</span>
    </h1>

    <address class="address">
      <span>4817 Ferncliff Rd</span>
      <span>Bay Hollow CA</span>
      <span>97352</span>
    </address>

    <p class="website">www.hlworks.com</p>
  </div>
</body>
</html>
```